Business Card Design Project - Industrial Motor Rep

Create a business card that utilizes our existing logo found on our website: www.brivanequipco.com

We are a Industrial Distributor with a focus on electric motors. We represent several key brands which can be found on our web site. Our customer base includes Consultants, Large End Users (VX, Harl Chemical, Telvo) and original equipment manufacturers.

Industry/Entity Type

Business

Requirements
Must have
• Name, Title, Phone, Fax, Cell, Website, Mailing address

```html
<!DOCTYPE html>
<html lang="en">
<head>
<meta charset="utf-8">
<title>Brivan Equipco – Business Card</title>
<link rel="stylesheet" href="https://fonts.googleapis.com/css2?family=Michroma&family=Source+Sans+3:wght@400;600&display=swap">
<style>
  :root {
    --backdrop: #2d2d2f;
    --card-light: #ffffff;
    --card-tint: #bfd3e6;
    --brand-blue: #1d5f9f;
    --accent-red: #e1283d;
    --ink: #3a3a3c;
  }
  * { box-sizing: border-box; margin: 0; padding: 0; }
  html, body {
    width: 1200px;
    height: 902px;
    overflow: hidden;
    background: var(--backdrop);
  }
  .stage {
    position: relative;
    width: 1200px;
    height: 902px;
  }
  .card {
    position: absolute;
    left: 242px;
    top: 245px;
    width: 716px;
    height: 411px;
    background: linear-gradient(100deg, var(--card-light) 0%, #e3ecf5 45%, var(--card-tint) 100%);
  }
  .holder {
    position: absolute;
    left: 50px;
    top: 46px;
  }
  .holder__name {
    font-family: "Michroma", sans-serif;
    font-size: 19px;
    letter-spacing: 4px;
    color: var(--brand-blue);
    line-height: 1.2;
  }
  .holder__title {
    font-family: "Michroma", sans-serif;
    font-size: 11px;
    letter-spacing: 3.4px;
    color: var(--accent-red);
    margin-top: 2px;
  }
  .contact {
    position: absolute;
    left: 50px;
    top: 245px;
    list-style: none;
    font-family: "Source Sans 3", sans-serif;
    font-size: 19px;
    color: var(--ink);
    line-height: 24px;
  }
  .contact__label {
    display: inline-block;
    width: 28px;
  }
  .brand {
    position: absolute;
    left: 500px;
    top: 262px;
    width: 190px;
    display: flex;
    flex-direction: column;
    align-items: center;
    gap: 12px;
  }
  .brand__dot {
    width: 62px;
    height: 62px;
    border-radius: 50%;
    background: var(--brand-blue);
  }
  .brand__name {
    font-family: "Source Sans 3", sans-serif;
    font-weight: 600;
    font-size: 26px;
    color: var(--brand-blue);
    letter-spacing: 0.5px;
    white-space: nowrap;
  }
</style>
</head>
<body>
  <main class="stage">
    <section class="card" aria-label="Business card front">
      <header class="holder">
        <h1 class="holder__name">JOHN DOE</h1>
        <p class="holder__title">DIRECTOR</p>
      </header>

      <ul class="contact">
        <li><span class="contact__label">T:</span> 999-999-9999</li>
        <li><span class="contact__label">M:</span>12345 67890</li>
        <li><span class="contact__label">F:</span> 999-999-9999</li>
        <li><span class="contact__label">E:</span> jdoe@brivanequipco.com</li>
        <li><span class="contact__label">W:</span>www.brivanequipco.com</li>
      </ul>

      <div class="brand">
        <span class="brand__dot" aria-hidden="true"></span>
        <span class="brand__name">Brivan Equipco</span>
      </div>
    </section>
  </main>
</body>
</html>
```